Tarn Bites menu + business card design

I want a menu design for my Food Truck.

I have attached the logo for it and my sliders will have different colors such as ( Black sliders, Red sliders and normal color) a picture will illustrates what I mean.

The menu should include:

Sliders:

Tarn Bite Single

Tarn Bites Meal

Fries:

Tarn Fries

Drinks:
Tarn Mojito

Water

VelaFizz

Desserts:

Charcoal cake

Target Market(s)

All

Industry/Entity Type

Business

Contact Information for Business Card

My theme is black and yellow like my logo

Colors

Designer to choose colors to be used in the design.

Requirements
Must have
• WhatsApp logo and the number for it is : +966500473829 " please dont squeeze the numbers".
• Instagram logo and my account is: TarnBites
• Snapchat logo and my account is: TarnBites
• Email logo and my email is: TheTarnBites@postvale.com
Nice to have
• Circle design of the whole business card but it is not a must
• i will attach a picture.

```html
<!DOCTYPE html>
<html lang="en">
<head>
<meta charset="utf-8">
<title>Tarn Bites – Business Card</title>
<link rel="stylesheet" href="https://fonts.googleapis.com/css2?family=Fredoka:wght@500;600&display=swap">
<style>
  :root {
    --night: #2b252e;
    --amber: #f9a81e;
    --ink: #231f22;
    --paper: #ffffff;
    --glasses-frame: #2a2a2a;
    --glasses-fill: #c0642a;
  }
  * { margin: 0; padding: 0; box-sizing: border-box; }
  html, body {
    width: 1200px;
    height: 800px;
    overflow: hidden;
    background: var(--night);
  }
  .card-stage { display: block; width: 1200px; height: 800px; }
  .card-disc { fill: var(--amber); }
  .ring-text {
    font-family: "Fredoka", sans-serif;
    font-weight: 500;
    fill: var(--paper);
  }
  .ring-text--phone { font-size: 42px; }
  .ring-text--handle { font-size: 38px; }
  .ring-text--email { font-size: 31px; }
  .icon-outline { fill: none; stroke: var(--paper); stroke-width: 5; stroke-linejoin: round; }
  .icon-solid { fill: var(--paper); }
  .brand-name {
    font-family: "Fredoka", sans-serif;
    font-weight: 600;
    font-size: 64px;
    fill: var(--ink);
    text-transform: uppercase;
  }
</style>
</head>
<body>
<svg class="card-stage" viewBox="0 0 1200 800" xmlns="http://www.w3.org/2000/svg">
  <defs>
    <path id="arc-top" d="M871.8 236 A300 300 0 0 0 352.2 236"/>
    <path id="arc-left" d="M459 121 A306 306 0 0 0 459 651"/>
    <path id="arc-right" d="M765 651 A306 306 0 0 0 765 121"/>
    <path id="arc-bottom" d="M350.5 537 A302 302 0 0 0 873.5 537"/>
  </defs>

  <circle class="card-disc" cx="612" cy="386" r="332"/>

  <!-- Phone -->
  <g class="phone-icon" transform="translate(756 136) scale(1.9)">
    <path class="icon-solid" d="M6.62 10.79c1.44 2.83 3.76 5.14 6.59 6.59l2.2-2.2c.27-.27.67-.36 1.02-.24 1.12.37 2.33.57 3.57.57.55 0 1 .45 1 1V20c0 .55-.45 1-1 1-9.39 0-17-7.61-17-17 0-.55.45-1 1-1h3.5c.55 0 1 .45 1 1 0 1.25.2 2.45.57 3.57.11.35.03.74-.25 1.02l-2.2 2.2z"/>
  </g>
  <text class="ring-text ring-text--phone">
    <textPath href="#arc-top" startOffset="52%" text-anchor="middle">+966500473829</textPath>
  </text>

  <!-- Photo-sharing handle -->
  <rect class="icon-outline" x="336" y="224" width="44" height="44" rx="11" transform="rotate(-22 358 246)"/>
  <text class="ring-text ring-text--handle">
    <textPath href="#arc-left" startOffset="50%" text-anchor="middle">TarnBites</textPath>
  </text>

  <!-- Chat app handle -->
  <circle class="icon-solid" cx="868" cy="528" r="22"/>
  <text class="ring-text ring-text--handle">
    <textPath href="#arc-right" startOffset="50%" text-anchor="middle">TarnBites</textPath>
  </text>

  <!-- Email -->
  <g class="mail-icon" transform="translate(401 597) rotate(40)">
    <rect class="icon-outline" x="-26" y="-18" width="52" height="36" rx="2"/>
    <polyline class="icon-outline" points="-26,-18 0,4 26,-18"/>
  </g>
  <text class="ring-text ring-text--email">
    <textPath href="#arc-bottom" startOffset="50%" text-anchor="middle">TheTarnBites@postvale.com</textPath>
  </text>

  <!-- Centre mark -->
  <rect role="img" aria-label="Illustration of sunglasses with burger layers in the lenses"
        x="492" y="304" width="242" height="88" rx="30" fill="var(--glasses-fill)"
        stroke="var(--glasses-frame)" stroke-width="8"/>
  <text class="brand-name" x="612" y="458" text-anchor="middle">Tarn</text>
  <text class="brand-name" x="612" y="512" text-anchor="middle">Bites</text>
</svg>
</body>
</html>
```